Statonary for Design Build Firm
Design Build company
Statonary for Design Build Firm -
Creative Brief
Professional
Peter L. Vondrasek
C.E.O.
Dubai UAE
US# 1-415-372-9054
mvelondrask@tmwrgroup.net
www.tmwrgroup.net

```html
<!DOCTYPE html>
<html lang="en">
<head>
<meta charset="utf-8">
<title>TMWR Group Stationery</title>
<link rel="stylesheet" href="https://fonts.googleapis.com/css2?family=Arimo:wght@400;700&display=swap">
<style>
  :root {
    --navy: #0b2656;
    --blue: #1d5ea8;
    --sky: #4c8fd6;
    --orange: #f07a1a;
    --paper: #ffffff;
    --stage: #f4f5f7;
    --ink: #2b2f36;
    --rule: #c9ccd1;
  }
  * { box-sizing: border-box; margin: 0; padding: 0; }
  html, body { width: 1200px; height: 681px; overflow: hidden; }
  body { background: var(--stage); font-family: "Arimo", Arial, sans-serif; color: var(--ink); position: relative; }
  address { font-style: normal; }

  .piece { position: absolute; background: var(--paper); box-shadow: 0 2px 6px rgba(0,0,0,.18); overflow: hidden; }
  .header-band { position: absolute; left: 0; top: 0; width: 100%; display: block; }

  .brand { position: absolute; display: flex; align-items: center; gap: 6px; }
  .brand-mark { background: var(--blue); flex: none; }
  .brand-name { font-weight: 700; color: var(--navy); white-space: nowrap; }
  .brand-tagline { position: absolute; color: var(--orange); white-space: nowrap; }

  /* envelope front */
  .envelope-front { left: 60px; top: 96px; width: 492px; height: 216px; }
  .envelope-front .header-band { height: 52px; }
  .envelope-front .brand { left: 18px; top: 60px; }
  .envelope-front .brand-mark { width: 22px; height: 22px; }
  .envelope-front .brand-name { font-size: 16px; }
  .envelope-front .brand-tagline { left: 46px; top: 86px; font-size: 5.5px; }

  /* envelope back */
  .envelope-back { left: 60px; top: 362px; width: 492px; height: 226px; }
  .envelope-back .flap { position: absolute; inset: 0; width: 100%; height: 100%; }
  .envelope-back .brand { left: 50%; top: 40px; transform: translateX(-50%); }
  .envelope-back .brand-mark { width: 16px; height: 16px; }
  .envelope-back .brand-name { font-size: 12px; }

  /* letterhead */
  .letterhead { left: 624px; top: 48px; width: 356px; height: 581px; }
  .letterhead .header-band { height: 58px; }
  .letterhead .brand { left: 16px; top: 44px; }
  .letterhead .brand-mark { width: 22px; height: 22px; }
  .letterhead .brand-name { font-size: 15px; }
  .letterhead .brand-tagline { left: 44px; top: 70px; font-size: 5px; }
  .office { position: absolute; top: 509px; font-size: 5px; line-height: 7px; color: var(--ink); }
  .office strong { font-weight: 700; }
  .office-left { left: 16px; }
  .office-right { right: 16px; text-align: right; }

  /* business card */
  .business-card { left: 941px; top: 204px; width: 235px; height: 103px; }
  .business-card .header-band { height: 36px; }
  .card-person { position: absolute; left: 10px; top: 8px; color: #fff; }
  .card-person .name { font-size: 6px; font-weight: 700; }
  .card-person .role { font-size: 4.5px; color: var(--orange); margin-top: 1px; }
  .business-card .brand { left: 118px; top: 44px; }
  .business-card .brand-mark { width: 14px; height: 14px; }
  .business-card .brand-name { font-size: 11px; }
  .card-contact { position: absolute; left: 10px; bottom: 8px; font-size: 4.5px; line-height: 6px; }
</style>
</head>
<body>

<svg width="0" height="0" style="position:absolute" aria-hidden="true">
  <defs>
    <linearGradient id="band-fill" x1="0" y1="0" x2="1" y2="0">
      <stop offset="0" stop-color="#0b2656"/>
      <stop offset="0.5" stop-color="#4c8fd6"/>
      <stop offset="1" stop-color="#0b2656"/>
    </linearGradient>
  </defs>
</svg>

<section class="piece envelope-front">
  <svg class="header-band" viewBox="0 0 100 20" preserveAspectRatio="none" aria-hidden="true">
    <polygon points="0,0 100,0 100,16 55,7 0,16" fill="url(#band-fill)"/>
    <polyline points="0,16 55,7 100,16" fill="none" stroke="var(--orange)" stroke-width="2" vector-effect="non-scaling-stroke"/>
  </svg>
  <div class="brand"><span class="brand-mark"></span><span class="brand-name">TMWR Group</span></div>
  <div class="brand-tagline">Design Build Contractors</div>
</section>

<section class="piece envelope-back">
  <svg class="flap" viewBox="0 0 492 226" aria-hidden="true">
    <polyline points="4,4 8,14 246,104 484,14 488,4" fill="none" stroke="var(--rule)" stroke-width="1"/>
    <line x1="4" y1="222" x2="160" y2="124" stroke="var(--rule)"/>
    <line x1="488" y1="222" x2="332" y2="124" stroke="var(--rule)"/>
  </svg>
  <div class="brand"><span class="brand-mark"></span><span class="brand-name">TMWR Group</span></div>
</section>

<section class="piece letterhead">
  <svg class="header-band" viewBox="0 0 100 20" preserveAspectRatio="none" aria-hidden="true">
    <polygon points="0,0 100,0 100,11 45,4 0,11" fill="url(#band-fill)"/>
    <polyline points="0,11 45,4 100,11" fill="none" stroke="var(--orange)" stroke-width="2" vector-effect="non-scaling-stroke"/>
  </svg>
  <div class="brand"><span class="brand-mark"></span><span class="brand-name">TMWR Group</span></div>
  <div class="brand-tagline">Design Build Contractors</div>
  <address class="office office-left">
    <strong>Dubai UAE</strong><br>
    Dubai Office +971 4 555 0182<br>
    Email: pvondrasek@tmwrgroup.net<br>
    Web: www.tmwrgroup.net
  </address>
  <address class="office office-right">
    <strong>Main Office</strong><br>
    US# 1-415-555-0147<br>
    Email: pvondrasek@tmwrgroup.net<br>
    Web: www.tmwrgroup.net
  </address>
</section>

<section class="piece business-card">
  <svg class="header-band" viewBox="0 0 100 20" preserveAspectRatio="none" aria-hidden="true">
    <polygon points="0,0 100,0 100,14 60,6 0,14" fill="url(#band-fill)"/>
    <polyline points="0,14 60,6 100,14" fill="none" stroke="var(--orange)" stroke-width="2" vector-effect="non-scaling-stroke"/>
  </svg>
  <div class="card-person">
    <div class="name">Peter L. Vondrasek</div>
    <div class="role">C.E.O.</div>
  </div>
  <div class="brand"><span class="brand-mark"></span><span class="brand-name">TMWR Group</span></div>
  <address class="card-contact">
    Dubai UAE<br>
    US# 1-415-555-0147<br>
    pvondrasek@tmwrgroup.net<br>
    www.tmwrgroup.net
  </address>
</section>

</body>
</html>
```